Salon website

Need a web design for a new blow dry and hair extension boutique in CT
would like the color scheme to be gray, white and tiffany blue
Create a web site with about 4 pages showing
1 about us page
1 blow dry services page
1 hair extension services page
1 contact us page
1 membership page
1 parties page

Industry/Entity Type

Boutique

Colors
86cfc6
cfeae6
33b7a4
aaaaaa
cbcbcb
ffffff

```html
<!DOCTYPE html>
<html lang="en">
<head>
<meta charset="utf-8">
<title>Crestline Blow Dry — About Us</title>
<link rel="stylesheet" href="https://fonts.googleapis.com/css2?family=Roboto+Condensed:wght@300;400&display=swap">
<style>
  :root{
    --tiffany:#86cfc6;
    --tiffany-light:#cfeae6;
    --tiffany-deep:#33b7a4;
    --graphite:#5d5d5d;
    --ink:#555555;
    --text:#666666;
    --muted:#aaaaaa;
    --rule:#e4e4e4;
    --dash:#f3e3b3;
    --white:#ffffff;
  }
  *{box-sizing:border-box;margin:0;padding:0}
  html,body{width:900px;height:1200px;overflow:hidden;background:var(--white)}
  body{position:relative;font-family:"Roboto Condensed",Arial,sans-serif;font-weight:300;color:var(--text)}
  .abs{position:absolute}

  /* header */
  .brand{left:45px;top:8px;width:140px;height:105px;background:var(--tiffany);box-shadow:0 0 6px rgba(0,0,0,.45);display:flex;align-items:center;justify-content:center}
  .brand-name{font-size:17px;color:var(--graphite);font-weight:400}
  .main-nav{left:0;top:0;height:88px;width:900px}
  .nav-item{position:absolute;top:0;height:88px;line-height:84px;font-size:14px;font-weight:300;color:var(--ink);text-transform:uppercase;text-align:center}
  .nav-item.is-active{background:var(--graphite);color:var(--tiffany);border-top:4px solid var(--tiffany);line-height:80px}
  .nav-item.is-active::after{content:"";position:absolute;left:50%;top:0;margin-left:-6px;border:6px solid transparent;border-top-color:var(--tiffany)}

  /* info band */
  .info-band{left:0;top:122px;width:900px;height:84px;background:var(--graphite)}
  .call-tab{left:45px;top:122px}
  .call-number{left:127px;top:140px;font-size:20px;color:var(--white);font-weight:300}
  .call-city{left:100px;top:179px;width:110px;text-align:center;font-size:11px;color:var(--white);font-weight:300}
  .hours{right:45px;top:146px;font-size:13px;color:var(--white);font-weight:300}
  .hours span{color:var(--tiffany)}

  /* breadcrumb */
  .crumbs{left:45px;top:248px;width:810px;height:46px;border-top:1px dashed var(--dash);border-bottom:1px dashed var(--dash);font-size:12px;font-weight:300}
  .crumbs .crumb{position:absolute;top:15px}
  .crumbs .home{left:0;color:var(--ink)}
  .crumbs .sep{left:42px;top:12px;width:1px;height:18px;background:var(--rule)}
  .crumbs .current{left:59px;color:var(--tiffany)}

  /* content */
  .section-title{font-size:19px;color:var(--tiffany);text-transform:uppercase;font-weight:300;padding-bottom:14px;border-bottom:1px solid var(--rule)}
  .who{left:45px;top:339px;width:235px}
  .photo{display:block}
  .who .photo{margin-top:12px;width:235px;height:165px;background:linear-gradient(135deg,#9aa3b5 0%,#c8bfa6 45%,#d9c89b 60%,#8c93a6 100%)}
  .lead{margin-top:14px;font-size:14.5px;line-height:22.5px;text-transform:uppercase;color:var(--text);font-weight:300}
  .body-copy{font-size:10px;line-height:16.5px;color:var(--ink);font-weight:300}
  .who .body-copy{margin-top:12px}
  .who .body-copy + .body-copy{margin-top:10px}

  .history{left:320px;top:339px;width:243px}
  .timeline{list-style:none;margin-top:14px}
  .timeline li{display:flex;height:76px}
  .timeline .year{width:37px;padding-top:9px;font-size:11px;color:#222;font-weight:300}
  .timeline .body-copy{width:210px;letter-spacing:-.15px}

  .experts{left:604px;top:339px;width:242px}
  .expert-name{font-size:14px;color:var(--ink);margin-top:14px;line-height:20px;font-weight:300}
  .expert-frame{width:209px;background:var(--white);padding:5px;box-shadow:0 1px 5px rgba(0,0,0,.35)}
  .expert-frame .photo{width:199px}
  .expert-one .photo{height:195px;background:linear-gradient(160deg,#4a4a4a 0%,#b9b2a2 45%,#e7e5e0 70%,#6c6c6c 100%)}
  .expert-two .photo{height:163px;background:linear-gradient(160deg,#8a7c6f 0%,#4a3b31 40%,#2f241e 65%,#a8743d 100%)}
  .expert-name.second{margin-top:8px}

  /* footer */
  .site-footer{left:0;top:865px;width:900px;height:285px;background:var(--graphite)}
  .foot-col{position:absolute;top:31px}
  .foot-title{font-size:16px;color:var(--tiffany);text-transform:uppercase;font-weight:300}
  .social{display:flex;gap:9px;margin-top:20px;padding-left:4px}
  .social-link{width:27px;height:33px;background:var(--white);border-radius:2px}
  .location-title{margin-top:22px;padding-bottom:6px;border-bottom:1px solid #666;width:170px}
  .foot-text{font-size:10.5px;line-height:20.5px;color:#dddddd;font-weight:300}
  .address{margin-top:6px;line-height:24.5px}
  .foot-col .foot-text.block{margin-top:19px}
  .read-more{display:block;color:var(--tiffany)}
  .quote-mark{font-family:Georgia,serif;font-size:44px;line-height:0;color:#333;font-weight:700;vertical-align:-15px}
  .quote-by{margin-top:4px;padding-left:73px;font-size:12px;color:#777;font-weight:300}
  .contact-lines{margin-top:17px;line-height:24.5px}

  .copyright{left:45px;top:1168px;font-size:11.5px;color:var(--ink);font-weight:300}
</style>
</head>
<body>

<header>
  <div class="abs brand" aria-label="Crestline Blow Dry">
    <span class="brand-name">Crestline Blow Dry</span>
  </div>
  <nav class="abs main-nav">
    <a class="nav-item" style="left:316px;width:60px">Home</a>
    <a class="nav-item is-active" style="left:384px;width:92px">About Us</a>
    <a class="nav-item" style="left:490px;width:66px">Services</a>
    <a class="nav-item" style="left:580px;width:90px">Membership</a>
    <a class="nav-item" style="left:694px;width:60px">Parties</a>
    <a class="nav-item" style="left:776px;width:70px">Contact</a>
  </nav>
</header>

<div class="abs info-band"></div>
<svg class="abs call-tab" width="220" height="84" viewBox="0 0 220 84">
  <polygon points="0,0 216,0 173,84 0,84" fill="#86cfc6"/>
  <circle cx="63" cy="31" r="15.5" fill="none" stroke="#ffffff" stroke-opacity=".7" stroke-width="1"/>
  <path d="M57 24 q-3 3 1 9 q4 6 9 7 q2 0 3-2 l-3-3 l-2 1 q-3-2-5-6 l1-2 z" fill="#ffffff"/>
</svg>
<div class="abs call-number">1234567890</div>
<div class="abs call-city">City Name</div>
<div class="abs hours">TIMMINGS : <span>09.30 AM - 10.00PM</span></div>

<div class="abs crumbs">
  <span class="crumb home">HOME</span>
  <span class="crumb sep"></span>
  <span class="crumb current">ABOUT US</span>
</div>

<main>
  <section class="abs who">
    <h2 class="section-title">Who We Are</h2>
    <div class="photo" role="img" aria-label="Portrait of a client with long blonde blow-dried hair"></div>
    <p class="lead">Lorem ipm dolor sit amet, consectetuer adipiscing elit. Praesent vestibulum.</p>
    <p class="body-copy">Lorem ipsum dolor sit amet, consectetuer adipiscing elit. Praesent vestibulum molestie lacus. Aeonummy hendrerit mauris. Phasellus porta. Fusce suscipit varius mi.</p>
    <p class="body-copy">Lorem ipsum dolor sit amet, consectetuer adipiscing elit. Praesent vestibulum molestie lacus. Aeonummy hendrerit mauris. Phasellus porta. Fusce suscipit varius mi.</p>
  </section>

  <section class="abs history">
    <h2 class="section-title">Our History</h2>
    <ol class="timeline">
      <li><span class="year">2012 -</span><p class="body-copy">Lorem ipsum dolor sit amet, consectetuer adipiscing elit. Praesent vestibulum molestie lacus. Aeonummy hendrerit mauris. Phasellus porta. Fusce suscipit varius mi.</p></li>
      <li><span class="year">2008 -</span><p class="body-copy">Lorem ipsum dolor sit amet, consectetuer adipiscing elit. Praesent vestibulum molestie lacus. Aeonummy hendrerit mauris. Phasellus porta. Fusce suscipit varius mi.</p></li>
      <li><span class="year">2005 -</span><p class="body-copy">Lorem ipsum dolor sit amet, consectetuer adipiscing elit. Praesent vestibulum molestie lacus. Aeonummy hendrerit mauris. Phasellus porta. Fusce suscipit varius mi.</p></li>
      <li><span class="year">2002 -</span><p class="body-copy">Lorem ipsum dolor sit amet, consectetuer adipiscing elit. Praesent vestibulum molestie lacus. Aeonummy hendrerit mauris. Phasellus porta. Fusce suscipit varius mi.</p></li>
      <li><span class="year">2000 -</span><p class="body-copy">Lorem ipsum dolor sit amet, consectetuer adipiscing elit. Praesent vestibulum molestie lacus. Aeonummy hendrerit mauris. Phasellus porta. Fusce suscipit varius mi.</p></li>
    </ol>
  </section>

  <section class="abs experts">
    <h2 class="section-title">Our Experts</h2>
    <p class="expert-name">expert name</p>
    <div class="expert-frame expert-one"><div class="photo" role="img" aria-label="Stylist portrait with sleek platinum hair and fringe"></div></div>
    <p class="expert-name second">expert name</p>
    <div class="expert-frame expert-two"><div class="photo" role="img" aria-label="Stylist portrait with voluminous dark curls"></div></div>
  </section>
</main>

<footer class="abs site-footer">
  <div class="foot-col" style="left:57px">
    <h3 class="foot-title">Follow Us</h3>
    <div class="social">
      <a class="social-link" aria-label="Social profile one"></a>
      <a class="social-link" aria-label="Social profile two"></a>
      <a class="social-link" aria-label="News feed"></a>
      <a class="social-link" aria-label="Social profile three"></a>
    </div>
    <h3 class="foot-title location-title">Location</h3>
    <p class="foot-text address">1-22-003-55,<br>Neque porro quisquam,<br>dolor sit amet,<br>your city.</p>
  </div>
  <div class="foot-col" style="left:263px;width:178px">
    <h3 class="foot-title">Information</h3>
    <p class="foot-text block">Lorem ipsum dolor sit amet, consectetur adipiscing elit, sed do eiusmod tempor incididunt ut labore et dolore magna aliqua. Ut enim ad minim veniam, quis nostrud exercitation ullamco laboris nisi ut aliquip ex ea commodo consequat. <a class="read-more">Read More[....]</a></p>
  </div>
  <div class="foot-col" style="left:469px;width:172px">
    <h3 class="foot-title">Testimonials</h3>
    <p class="foot-text block"><span class="quote-mark">&ldquo;</span> Lorem ipsum dolor sit amet, consectetur adipiscing elit, sed do eiusmod tempor incididunt ut labore et dolore magna aliqua. Ut enim ad minim veniam, quis nostrud exercitation ullamco laboris nisi ut aliquip ex ea commodo consequat. <span class="quote-mark">&rdquo;</span></p>
    <p class="quote-by">- Lorem ipsum dolor</p>
  </div>
  <div class="foot-col" style="left:675px;width:180px">
    <h3 class="foot-title">Contact Us</h3>
    <p class="foot-text contact-lines">hello(at)crestlineblowdry.com<br>Mobile : +12 345 67890<br>Telephone : +00 000 00000<br>Fax : +00 000 00000</p>
  </div>
</footer>

<p class="abs copyright">Company Name © 2014 All Rights Reseverd</p>

</body>
</html>
```